Composite decking sales poster

Poster advertising our brand of decking and our industry-best warranty.
Poster dimensions 1200mm wide x 400mm high.
50 Year Stain and Fade Warranty.
Ultra-Low Maintenance.
Environmentally Friendly Made from Recycled Materials.
Website: https://velmorboards.com.au
Phone: 1300 482 937
*** Uploaded pictures are optional to use ***
Must list website, phone number and logos.

```html
<!DOCTYPE html>
<html lang="en">
<head>
<meta charset="utf-8">
<title>Velmor Composite Decking Poster</title>
<link rel="stylesheet" href="https://fonts.googleapis.com/css2?family=Poppins:wght@300;400;600;700&display=swap">
<style>
  :root {
    --backdrop: #c1c1c1;
    --paper: #ffffff;
    --panel-blue: rgba(62, 110, 170, 0.82);
    --brand-blue: #3f6ea3;
    --ink: #111111;
    --logo-ink: #3b3b3d;
  }
  * { margin: 0; padding: 0; box-sizing: border-box; }
  html, body {
    width: 1200px;
    height: 931px;
    overflow: hidden;
    background: var(--backdrop);
    font-family: "Poppins", sans-serif;
  }
  .poster {
    position: absolute;
    left: 55px;
    top: 304px;
    width: 1090px;
    height: 363px;
    background: var(--paper);
    overflow: hidden;
  }
  .poster-art {
    position: absolute;
    inset: 0;
    width: 1090px;
    height: 363px;
  }
  .intro-panel {
    position: absolute;
    left: 0;
    top: 14px;
    width: 352px;
    height: 170px;
    background: var(--panel-blue);
    border-radius: 0 0 42px 0;
    color: #fff;
    padding: 12px 0 0 38px;
  }
  .headline {
    font-weight: 400;
    font-size: 21px;
    line-height: 26px;
    letter-spacing: 0.1px;
  }
  .intro-copy {
    margin-top: 16px;
    font-weight: 300;
    font-size: 13.2px;
    line-height: 15.6px;
    width: 300px;
  }
  .benefits {
    position: absolute;
    left: 38px;
    top: 258px;
    list-style: none;
  }
  .benefits li {
    display: flex;
    align-items: center;
    height: 28.3px;
    font-weight: 700;
    font-size: 15.8px;
    color: var(--ink);
  }
  .tick {
    width: 12px;
    height: 12px;
    margin-right: 12px;
    flex: none;
  }
  .contact {
    position: absolute;
    left: 599px;
    top: 297px;
    border-left: 1px solid var(--brand-blue);
    padding-left: 6px;
    height: 42px;
  }
  .contact-phone {
    font-weight: 700;
    font-size: 20px;
    line-height: 22px;
    color: var(--brand-blue);
  }
  .contact-web {
    font-weight: 400;
    font-size: 15.8px;
    line-height: 20px;
    color: var(--ink);
  }
  .brand {
    position: absolute;
    left: 870px;
    top: 294px;
    display: flex;
    align-items: center;
    gap: 12px;
  }
  .brand-square {
    width: 24px;
    height: 24px;
    background: var(--brand-blue);
  }
  .brand-name {
    font-weight: 600;
    font-size: 34px;
    line-height: 40px;
    color: var(--logo-ink);
  }
</style>
</head>
<body>
  <main class="poster">
    <svg class="poster-art" viewBox="0 0 1090 363" xmlns="http://www.w3.org/2000/svg">
      <defs>
        <linearGradient id="poolTone" x1="0" y1="0" x2="1" y2="1">
          <stop offset="0" stop-color="#2f86bd"/>
          <stop offset="1" stop-color="#3aa3d4"/>
        </linearGradient>
        <linearGradient id="deckTone" x1="0" y1="0" x2="1" y2="0">
          <stop offset="0" stop-color="#8f8a8c"/>
          <stop offset="0.3" stop-color="#a39ea0"/>
          <stop offset="0.4" stop-color="#ececec"/>
          <stop offset="0.55" stop-color="#e6e6e6"/>
          <stop offset="0.68" stop-color="#a29d9f"/>
          <stop offset="1" stop-color="#8b8688"/>
        </linearGradient>
        <linearGradient id="timberTone" x1="0" y1="0" x2="1" y2="1">
          <stop offset="0" stop-color="#6e4f46"/>
          <stop offset="0.5" stop-color="#5b423c"/>
          <stop offset="1" stop-color="#7a5a4f"/>
        </linearGradient>
      </defs>
      <rect class="pool-photo" x="0" y="0" width="366" height="226" fill="url(#poolTone)"
            role="img" aria-label="Photo of a blue mosaic-tiled swimming pool"/>
      <path class="deck-photo" fill="url(#deckTone)"
            d="M366 0 H1090 V118 H920 V140 H640 C560 175 480 226 410 226 H366 Z"
            role="img" aria-label="Photo of grey composite decking beside a pool with a coffee cup, laptop and white towel"/>
      <path class="timber-frame" fill="#ffffff"
            d="M626 38 H880 A42 42 0 0 1 922 80 V262 H626 Z"/>
      <path class="timber-photo" fill="url(#timberTone)"
            d="M630 42 H876 A36 36 0 0 1 912 78 V258 H672 A42 42 0 0 1 630 216 Z"
            role="img" aria-label="Photo of brown composite decking boards laid in a herringbone pattern"/>
    </svg>

    <section class="intro-panel">
      <h1 class="headline">BEAUTIFUL OUTDOOR LIVING.<br>BUILT FOR LIFE.</h1>
      <p class="intro-copy">From the beauty of its dramatic colour tones and multiple wood grain patterns to the polish and protection of Kovralith capping, Velmor is the decking board for those who won’t compromise.</p>
    </section>

    <ul class="benefits">
      <li><svg class="tick" viewBox="0 0 12 12"><circle cx="6" cy="6" r="6" fill="#3f6ea3"/><path d="M3.3 6.1 L5.2 7.9 L8.7 4.3" fill="none" stroke="#fff" stroke-width="1.5" stroke-linecap="round" stroke-linejoin="round"/></svg>50 Year Stain and Fade Warranty.</li>
      <li><svg class="tick" viewBox="0 0 12 12"><circle cx="6" cy="6" r="6" fill="#3f6ea3"/><path d="M3.3 6.1 L5.2 7.9 L8.7 4.3" fill="none" stroke="#fff" stroke-width="1.5" stroke-linecap="round" stroke-linejoin="round"/></svg>Ultra-Low Maintenance.</li>
      <li><svg class="tick" viewBox="0 0 12 12"><circle cx="6" cy="6" r="6" fill="#3f6ea3"/><path d="M3.3 6.1 L5.2 7.9 L8.7 4.3" fill="none" stroke="#fff" stroke-width="1.5" stroke-linecap="round" stroke-linejoin="round"/></svg>Environmentally Friendly Made from Recycled Materials.</li>
    </ul>

    <div class="contact">
      <p class="contact-phone">1300 482 937</p>
      <p class="contact-web">www.velmorboards.com.au</p>
    </div>

    <div class="brand">
      <span class="brand-square"></span>
      <span class="brand-name">Velmor</span>
    </div>
  </main>
</body>
</html>
```